Kestrel Bridge Consulting (KBC) Business Card Design

I would like to create double-sided business cards that contain:
1) Name: Derek Molvane
2) Phone Number: +1 (555) 218-4907
3) Email: Derek.Molvane@KestrelBridgeConsulting.example
4) Website: KestrelBridgeConsulting.example

I would like to include my logo and a color scheme similar to the Varnholt Grand Prix Ostera squad color scheme (black, silver, greenish-blue – but can also include regular blue)

What we do: Our company develops and delivers innovative and pragmatic information technology and cybersecurity risk and compliance solutions for organizations in the commercial market as well as the federal, and state/local sectors.

```html
<!DOCTYPE html>
<html lang="en">
<head>
<meta charset="utf-8">
<title>Kestrel Bridge Consulting — Business Card</title>
<link href="https://fonts.googleapis.com/css2?family=Arimo:wght@400;700&display=swap" rel="stylesheet">
<style>
  :root {
    --backdrop: #1d1e20;
    --card-white: #f7f7f7;
    --ink-dark: #111827;
    --navy: #0b1f3a;
    --brand-blue: #0a84e6;
    --cyan-glow: #00d8ee;
    --blue-edge: #0a6be0;
    --white: #ffffff;
    --grey-text: #222222;
  }
  * { box-sizing: border-box; margin: 0; padding: 0; }
  html, body { width: 1200px; height: 750px; overflow: hidden; }
  body {
    background: var(--backdrop);
    font-family: "Arimo", Arial, sans-serif;
    position: relative;
  }
  .card {
    position: absolute;
    width: 520px;
    height: 300px;
    border-radius: 18px;
    overflow: hidden;
  }
  /* Front side */
  .card-front {
    left: 90px;
    top: 80px;
    background: var(--card-white);
  }
  .front-brand {
    position: absolute;
    left: 0; right: 0;
    top: 92px;
    display: flex;
    justify-content: center;
    align-items: center;
    gap: 16px;
  }
  .brand-dot {
    width: 62px; height: 62px;
    border-radius: 50%;
    background: var(--brand-blue);
  }
  .brand-name {
    font-weight: 400;
    font-size: 21px;
    line-height: 1.05;
    letter-spacing: 1.5px;
    text-transform: uppercase;
    color: var(--ink-dark);
    border-left: 1px solid var(--ink-dark);
    padding-left: 12px;
  }
  .front-web {
    position: absolute;
    left: 0; right: 0;
    bottom: 52px;
    text-align: center;
    font-size: 11px;
    font-weight: 700;
    letter-spacing: 2.6px;
    color: var(--grey-text);
  }
  /* Back side */
  .card-back {
    left: 590px;
    top: 370px;
    background: radial-gradient(ellipse at 58% 50%, var(--cyan-glow) 0%, #08aef0 38%, var(--blue-edge) 100%);
  }
  .back-brand {
    position: absolute;
    left: 40px;
    top: 90px;
    width: 130px;
    display: flex;
    flex-direction: column;
    align-items: center;
    gap: 10px;
  }
  .back-brand .brand-dot {
    width: 80px; height: 80px;
    background: var(--white);
  }
  .back-brand-name {
    font-size: 12px;
    font-weight: 400;
    text-align: center;
    letter-spacing: 0.8px;
    text-transform: uppercase;
    color: var(--white);
    line-height: 1.2;
  }
  .divider {
    position: absolute;
    left: 190px;
    top: 70px;
    width: 1px;
    height: 160px;
    background: var(--navy);
  }
  .contact {
    position: absolute;
    left: 208px;
    top: 84px;
    color: var(--white);
  }
  .person-name {
    font-size: 22px;
    font-weight: 700;
    color: var(--navy);
    text-transform: uppercase;
    letter-spacing: 0.3px;
  }
  .person-role {
    font-size: 15px;
    margin-top: 2px;
  }
  .contact-list {
    list-style: none;
    margin-top: 22px;
    font-size: 12.5px;
    line-height: 1.45;
  }
</style>
</head>
<body>
  <section class="card card-front" aria-label="Business card front">
    <div class="front-brand">
      <span class="brand-dot"></span>
      <div class="brand-name">Kestrel<br>Bridge<br>Consulting</div>
    </div>
    <p class="front-web">www.KestrelBridgeConsulting.example</p>
  </section>

  <section class="card card-back" aria-label="Business card back">
    <div class="back-brand">
      <span class="brand-dot"></span>
      <span class="back-brand-name">Kestrel Bridge<br>Consulting</span>
    </div>
    <div class="divider"></div>
    <div class="contact">
      <h1 class="person-name">Derek Molvane</h1>
      <p class="person-role">President</p>
      <ul class="contact-list">
        <li>+1 (555) 218-4907</li>
        <li>Derek.Molvane@KestrelBridgeConsulting.example</li>
        <li>www.KestrelBridgeConsulting.example</li>
      </ul>
    </div>
  </section>
</body>
</html>
```